Technology management company looking for a new website with a professional look

Brennick IT is a recently re-branded technology management company that is looking for a website design to match its personalized approach and friendly culture.

We would like to see a specialized, but related, page style for each of our main service offerings of:

• Commercial IT Support (This is our primary focus)
• Commercial Phone Systems (We partner with http://www.voxtrell.com/ for our phone systems)
• Point of Sale Systems (We partner with http://www.tillmora.com/ for our POS systems.
• Web Design
• Hollow Pine Computers (Our residential computer service offering, branded as Hollow Pine Computers)

The Hollow Pine Computers page should be build upon the Hollow Pine Computers logo, the other four pages should be branded as Brennick IT.

These five separate pages should have subtle, yet clearly defined links to one another. They should also each have a Home, Products, Service, and Company in the menu.

The website should have a clean design with professional appeal, but not appear too sterile or uninviting. It needs to have a simple, easy to navigate menu interface along the top. We would also like the site to be mobile friendly.

It should also allow us to easily tie in links to our social media pages (Facebook, LinkedIn, Twitter and Google+) and provide easy access to our contact information from each page.

This is a link to our old website www.hollowpinecomputers.com

We don't currently have copy available. The text and menu design should be easily editable and expandable so we can use the design to fit our copy.

In general we are looking for a concept we can modify to fit our needs.

We need this design to be available with layers in a .psd format.

Target Market(s)

Small to mid-size businesses.

Industry/Entity Type

Information Technology

Number of Pages Required

5+ page

Font styles to use
Sans Serif

Requirements
Must have
• Mobile Friendly
• Professional Type Face
• Unity between all pages
• .PSD Format
Nice to have
• Themed with our logo
Should not have
• Bubbly unprofessional typeface. No comic sans.

```html
<!DOCTYPE html>
<html lang="en">
<head>
<meta charset="utf-8">
<title>Brennick IT — Commercial IT Support</title>
<link href="https://fonts.googleapis.com/css2?family=Lato:ital,wght@0,400;0,700;0,900;1,400;1,700&display=swap" rel="stylesheet">
<style>
:root{
  --navy:#1c3d6e;
  --blue:#1f4f8f;
  --orange:#f26a21;
  --text:#555b63;
  --muted:#8a9098;
  --rule:#dcdfe3;
  --band:#f1f2f4;
  --footer:#3b3d41;
  --white:#ffffff;
}
*{margin:0;padding:0;box-sizing:border-box}
html,body{width:1200px;height:3604px;overflow:hidden}
body{font-family:'Lato',Arial,sans-serif;color:var(--text);background:var(--white);position:relative}

/* header */
.site-header{position:absolute;top:0;left:0;width:1200px;height:92px;background:var(--white)}
.top-contact{position:absolute;right:40px;top:8px;font-size:12px;color:var(--muted);display:flex;gap:22px}
.top-contact span{display:flex;align-items:center;gap:6px}
.brand{position:absolute;left:40px;top:26px;display:flex;align-items:center;gap:12px}
.brand-dot{width:34px;height:34px;border-radius:50%;background:var(--orange)}
.brand-name{font-size:34px;font-weight:900;color:var(--navy);letter-spacing:-.5px}
.main-nav{position:absolute;right:40px;top:56px;display:flex;gap:30px;font-size:14px;font-weight:700;color:var(--navy)}
.main-nav .active{color:var(--orange);border-bottom:2px solid var(--orange);padding-bottom:4px}

.service-nav{position:absolute;top:92px;left:0;width:1200px;height:40px;background:var(--blue);display:flex;justify-content:center;align-items:center;gap:0}
.service-nav a{color:var(--white);text-decoration:none;font-size:14px;font-weight:700;padding:0 22px;line-height:40px}
.service-nav a.current{background:var(--orange)}

/* hero */
.hero{position:absolute;top:132px;left:0;width:1200px;height:588px;background:radial-gradient(ellipse at 50% 55%,#6f8fb5 0%,#2c4463 40%,#121e2e 100%)}
.hero-title{position:absolute;top:118px;left:0;width:100%;text-align:center;font-size:36px;font-style:italic;font-weight:700;color:var(--white)}
.hero-title em{color:var(--orange);font-weight:900}
.hero-art{position:absolute;left:230px;top:190px;width:740px;height:370px;border-radius:8px;background:linear-gradient(160deg,#b9c9dc 0%,#5c7da3 50%,#22344c 100%);opacity:.7}

/* partners */
.partners{position:absolute;top:720px;left:0;width:1200px;height:120px;background:linear-gradient(#ffffff,#eceef1);display:flex;justify-content:center;align-items:center;gap:60px}
.badge{width:120px;height:50px;background:#c9ced5;border-radius:4px}
.badge.wide{width:140px}

/* intro */
.intro{position:absolute;top:870px;left:0;width:1200px;text-align:center}
.section-title{font-size:34px;font-weight:900;color:var(--navy);display:flex;justify-content:center;align-items:center;gap:12px}
.section-title .accent{color:var(--orange)}
.title-dot{width:26px;height:26px;border-radius:50%;background:var(--orange)}
.intro p{width:860px;margin:24px auto 0;font-size:16px;line-height:26px;color:var(--text)}
.rule{position:absolute;left:120px;width:960px;height:1px;background:var(--rule)}

.side-tab{position:absolute;right:0;top:880px;width:26px;height:100px;background:var(--orange);color:var(--white);font-size:10px;font-weight:900;writing-mode:vertical-rl;display:flex;align-items:center;justify-content:center;letter-spacing:1px}

/* services */
.service{position:absolute;left:120px;width:960px;height:280px}
.service-photo{position:absolute;top:30px;width:210px;height:210px;border-radius:50%;border:6px solid #e9ebee}
.service.left .service-photo{left:20px}
.service.right .service-photo{right:20px}
.service-body{position:absolute;top:44px;width:680px}
.service.left .service-body{left:270px}
.service.right .service-body{left:0}
.service h3{font-size:17px;font-weight:900;color:var(--navy);margin-bottom:10px}
.service p{font-size:13px;line-height:20px;color:var(--text)}
.service p.more{margin-top:14px}
.service p.more a{color:var(--orange);font-weight:700;text-decoration:none}

/* testimonials */
.clients{position:absolute;top:2580px;left:0;width:1200px;height:460px;background:var(--band);text-align:center}
.clients .section-title{margin-top:44px}
.client-mark{width:110px;height:110px;border-radius:50%;background:#1a1a1a;margin:30px auto 0;display:flex;align-items:center;justify-content:center;color:var(--white);font-size:20px;font-weight:900}
.quote{width:860px;margin:30px auto 0;font-size:15px;line-height:24px;font-style:italic;color:var(--text)}
.quote-author{margin-top:18px;font-size:16px;font-weight:900;color:var(--navy)}

/* map + contact */
.map{position:absolute;top:3040px;left:0;width:1200px;height:380px;background:linear-gradient(135deg,#e8e4da 0%,#dcd8cd 60%,#cfd8c4 100%)}
.contact-card{position:absolute;top:3060px;left:820px;width:340px;height:340px;background:var(--white);box-shadow:0 2px 10px rgba(0,0,0,.15);padding:20px 24px;text-align:center}
.contact-card .section-title{font-size:26px}
.field{height:28px;border:1px solid var(--rule);margin-top:10px;text-align:left;padding-left:8px;font-size:12px;line-height:26px;color:var(--muted)}
.field.area{height:60px}
.send-btn{margin:12px auto 0;width:170px;height:30px;background:var(--orange);color:var(--white);font-size:12px;font-weight:900;line-height:30px}
.contact-lines{margin-top:14px;font-size:12px;line-height:18px;color:var(--navy);font-weight:700}

/* footer */
.site-footer{position:absolute;top:3420px;left:0;width:1200px;height:184px;background:var(--footer);text-align:center;color:#cfd2d6}
.footer-brand{display:flex;justify-content:center;align-items:center;gap:10px;margin-top:30px}
.footer-brand .brand-dot{width:28px;height:28px}
.footer-brand .brand-name{color:var(--white);font-size:28px}
.footer-nav{margin-top:18px;font-size:13px;font-weight:700;display:flex;justify-content:center;gap:26px}
.footer-sub{margin-top:12px;font-size:12px;display:flex;justify-content:center;gap:20px;color:#a9adb3}
</style>
</head>
<body>

<header class="site-header">
  <div class="top-contact">
    <span><svg width="12" height="12" viewBox="0 0 24 24"><path fill="#f26a21" d="M6.6 10.8a15 15 0 0 0 6.6 6.6l2.2-2.2c.3-.3.7-.4 1-.2 1.1.4 2.3.6 3.6.6.6 0 1 .4 1 1V20c0 .6-.4 1-1 1A17 17 0 0 1 3 4c0-.6.4-1 1-1h3.5c.6 0 1 .4 1 1 0 1.3.2 2.5.6 3.6.1.3 0 .7-.2 1z"/></svg>555-014-2290</span>
    <span><svg width="12" height="12" viewBox="0 0 24 24"><path fill="#f26a21" d="M2 5h20v14H2zm2 2v.5l8 5 8-5V7z"/></svg>hello@brennickit.com</span>
  </div>
  <div class="brand"><span class="brand-dot"></span><span class="brand-name">Brennick IT</span></div>
  <nav class="main-nav">
    <span>HOME</span><span>PRODUCTS</span><span class="active">SERVICE</span><span>COMPANY</span>
  </nav>
</header>

<nav class="service-nav">
  <a class="current">Commercial IT Support</a>
  <a>Commercial Phone Systems</a>
  <a>Point of Sale Systems</a>
  <a>Web Design</a>
  <a>Hollow Pine Computers</a>
</nav>

<section class="hero">
  <h1 class="hero-title">Professional IT Support <em>CUSTOMIZED</em> to Meet Your Needs</h1>
  <div class="hero-art" role="img" aria-label="Cloud of connected laptops, tablets and phones around a glowing globe"></div>
</section>

<section class="partners">
  <div class="badge" role="img" aria-label="Partner certification badge"></div>
  <div class="badge" role="img" aria-label="Partner certification badge"></div>
  <div class="badge wide" role="img" aria-label="Certification badge"></div>
</section>

<div class="side-tab">CONTACT US</div>

<section class="intro">
  <h2 class="section-title"><span class="title-dot"></span>Commercial <span class="accent">IT SUPPORT</span></h2>
  <p>We offer a wide variety of services for our commercial clients, depending on the scope of their business and clientele. Click on one of the services to the left for more detailed information on several of the areas we specialize in. And of course, if you don't see your need listed, give us a call and we will see how we can help!</p>
</section>
<div class="rule" style="top:1080px"></div>

<section class="service left" style="top:1100px">
  <div class="service-photo" role="img" aria-label="Blue network cables plugged into a switch" style="background:radial-gradient(circle,#6d9ad0,#1f3f6e)"></div>
  <div class="service-body">
    <h3>NETWORK MANAGEMENT</h3>
    <p>We plan, build and watch over the networks that keep your office running. From switches and firewalls to wireless coverage, our team keeps every connection fast, secure and documented. We monitor traffic around the clock, apply updates on schedule and step in before small faults turn into costly downtime for your staff and customers.</p>
    <p class="more">For further information on the Network Management, please <a>contact us.</a></p>
  </div>
</section>
<div class="rule" style="top:1380px"></div>

<section class="service right" style="top:1380px">
  <div class="service-photo" role="img" aria-label="Technician working on a server rack" style="background:radial-gradient(circle,#8c9099,#2b2f36)"></div>
  <div class="service-body">
    <h3>ON-SITE &amp; REMOTE SUPPORT</h3>
    <p>When something breaks, you need help quickly. Our technicians can connect remotely within minutes to fix most problems, and when a visit is needed we come to your door. Desktops, printers, servers and user accounts are all covered, with clear notes on what we did so your team always knows where things stand.</p>
    <p class="more">For further information on the On-Site &amp; Remote Support, please <a>contact us.</a></p>
  </div>
</section>
<div class="rule" style="top:1660px"></div>

<section class="service left" style="top:1660px">
  <div class="service-photo" role="img" aria-label="Business team meeting around a table" style="background:radial-gradient(circle,#e6dccf,#8b7a66)"></div>
  <div class="service-body">
    <h3>IT CONSULTING</h3>
    <p>Technology decisions shape how your business grows. We sit down with you to understand your goals, review the systems you already have and map out a practical plan. Whether you are choosing new software, budgeting for hardware or planning for security, our advice is honest, clear and built around your needs.</p>
    <p class="more">For further information on the IT Consulting, please <a>contact us.</a></p>
  </div>
</section>
<div class="rule" style="top:1940px"></div>

<section class="service right" style="top:1940px">
  <div class="service-photo" role="img" aria-label="Glowing blue circuit board with cloud symbol" style="background:radial-gradient(circle,#7fc0f0,#0d3a78)"></div>
  <div class="service-body">
    <h3>CLOUD COMPUTING</h3>
    <p>Move your files, email and applications to the cloud with confidence. We help you pick the right services, migrate your data safely and set up backups that run on their own. Your team can work from anywhere on any device, while we handle the security, licensing and everyday upkeep behind the scenes.</p>
    <p class="more">For further information on the Cloud Computing, please <a>contact us.</a></p>
  </div>
</section>
<div class="rule" style="top:2220px"></div>

<section class="service left" style="top:2220px">
  <div class="service-photo" role="img" aria-label="Office desk with computer monitors ready to move" style="background:radial-gradient(circle,#d9dde2,#6f7782)"></div>
  <div class="service-body">
    <h3>IT OFFICE MOVES</h3>
    <p>Relocating your office is stressful enough without worrying about technology. We plan every step of the move, from labeling cables to setting up internet service at the new location. Your computers, phones and network are packed, moved and tested so your staff can sit down and start working on day one.</p>
    <p class="more">For further information on the IT Office Moves, please <a>contact us.</a></p>
  </div>
</section>

<section class="clients">
  <h2 class="section-title"><span class="title-dot"></span>Our <span class="accent">HAPPY CLIENTS</span></h2>
  <div class="client-mark">Ridgeway</div>
  <p class="quote">Brennick IT has been a real partner to our business. Their team answers quickly, explains problems in plain language and always follows through. Since they took over our systems we have had fewer outages, better security and far less stress. We recommend them to every business owner we know.</p>
  <p class="quote-author">Marcus Ellery, Ridgeway</p>
</section>

<section class="map" role="img" aria-label="Street map showing the office location"></section>
<aside class="contact-card">
  <h2 class="section-title"><span class="title-dot" style="width:20px;height:20px"></span>Get <span class="accent">IN TOUCH</span></h2>
  <div class="field">Name</div>
  <div class="field">Email</div>
  <div class="field area">Message</div>
  <div class="send-btn">SEND A MESSAGE</div>
  <div class="contact-lines">555-014-2290<br>hello@brennickit.com<br>412 Larkspur Ave. Suite 7, Fernwick, IN 46999</div>
</aside>

<footer class="site-footer">
  <div class="footer-brand"><span class="brand-dot"></span><span class="brand-name">Brennick IT</span></div>
  <nav class="footer-nav"><span>HOME</span><span>PRODUCTS</span><span>SERVICE</span><span>COMPANY</span></nav>
  <nav class="footer-sub"><span>Commercial IT Support</span><span>Commercial Phone Systems</span><span>Point of Sale Systems</span><span>Web Design</span><span>Hollow Pine Computers</span></nav>
</footer>

</body>
</html>
```